Alloy wheel repair business needs a website

Install logo previously purchased from pixelbazaar, toolbar with dropdowns. services, gallery, clients , contact ect
Maybe mission statment

Target Market(s)

vehicle owners, auto dealers,insurance companies,

Industry/Entity Type

Alloy Wheel Repair

Coding

Coded - Design and coding required

Number of Pages Required

4 page

Font styles to use
Sans Serif

Colors
0054AA
0677BA
7BADD7
CADEEF
E8F1F8

```html
<!DOCTYPE html>
<html lang="en">
<head>
<meta charset="utf-8">
<title>Velorim Repair – Alloy Wheel Repair</title>
<link rel="stylesheet" href="https://fonts.googleapis.com/css2?family=Poppins:wght@400;500;600;700&display=swap">
<style>
:root{
  --brand-deep:#0054AA;
  --brand:#0A76C6;
  --wave:#4A89C9;
  --sky:#7BADD7;
  --mist:#CADEEF;
  --ice:#E8F1F8;
  --ink:#333333;
  --white:#ffffff;
}
*{margin:0;padding:0;box-sizing:border-box}
html,body{width:1200px;height:3898px;overflow:hidden;background:var(--white)}
body{position:relative;font-family:'Poppins',sans-serif;color:var(--ink)}
a{color:inherit;text-decoration:none}

/* header */
.site-header{position:absolute;left:0;top:0;width:1200px;height:124px;background:var(--white)}
.brand{position:absolute;left:106px;top:50px;display:flex;align-items:center;gap:8px;font-size:22px;font-weight:700;color:var(--brand-deep);letter-spacing:1px;line-height:1;white-space:nowrap}
.brand-dot{width:14px;height:14px;border-radius:50%;background:var(--brand-deep)}
.main-nav a{position:absolute;top:54px;font-size:15px;color:var(--brand);text-transform:uppercase;white-space:nowrap}

/* hero */
.hero-wave{position:absolute;left:0;top:124px}
.hero-photo{position:absolute;left:177px;top:267px;width:346px;height:346px;border-radius:50%;background:radial-gradient(circle at 60% 50%,#c9ccd2 0%,#8a8f98 28%,#2a2c33 52%,#1d3f8a 78%,#152f6c 100%)}
.hero-title{position:absolute;left:583px;top:196px;width:520px;font-size:32px;font-weight:700;color:var(--white);line-height:40px}
.hero-text{position:absolute;left:584px;top:302px;width:480px;font-size:18px;line-height:27px;color:var(--white)}
.btn-solid{position:absolute;left:585px;top:421px;width:156px;height:44px;background:var(--white);color:var(--brand);font-size:18px;display:flex;align-items:center;justify-content:center}

/* about */
.about{position:absolute;left:88px;top:799px;width:1032px;height:534px}
.about-panel{position:absolute;left:0;top:0;width:584px;height:534px;background:var(--brand)}
.about-photo{position:absolute;left:584px;top:0;width:448px;height:534px;background:radial-gradient(circle at 50% 55%,#e6e6e6 0%,#9a9a9a 25%,#3a3a3a 50%,#1c1c1c 80%)}
.about h2{position:absolute;left:91px;top:76px;font-size:52px;font-weight:600;color:var(--white);line-height:72px}
.about p{position:absolute;left:91px;top:168px;width:380px;font-size:18.5px;line-height:24px;color:var(--white);font-weight:500}
.btn-outline{position:absolute;left:86px;top:401px;width:157px;height:45px;border:1.5px solid var(--white);border-radius:23px;color:var(--white);font-size:18px;display:flex;align-items:center;justify-content:center}

/* section titles */
.section-title{position:absolute;left:0;width:1200px;text-align:center;font-size:40px;font-weight:600;color:var(--ink);text-transform:uppercase}

/* services */
.service-card{position:absolute;top:1493px;width:318px;height:298px;background:var(--brand)}
.service-card .thumb{position:absolute;left:14px;top:12px;width:290px;height:223px}
.service-card h3{position:absolute;left:0;top:258px;width:100%;text-align:center;font-size:20px;font-weight:600;color:var(--white)}

/* mission */
.mission{position:absolute;left:86px;top:1909px;width:1031px;height:339px;background:var(--brand)}
.mission-photo{position:absolute;left:0;top:0;width:462px;height:339px;background:linear-gradient(120deg,#5a5d63 0%,#8c96a4 40%,#aac3d6 75%,#c7d4de 100%)}
.mission h2{position:absolute;left:521px;top:58px;font-size:53px;font-weight:600;color:var(--white);line-height:72px}
.mission p{position:absolute;left:523px;top:152px;width:365px;font-size:20.5px;line-height:24px;color:var(--white);font-weight:500}

/* gallery */
.gallery-item{position:absolute}

/* clients */
.clients-title{position:absolute;left:0;top:3102px;width:1200px;text-align:center;font-size:52px;font-weight:700;font-variant:small-caps;color:#3B82C4;letter-spacing:1px}
.carousel-btn{position:absolute;top:3218px;width:64px;height:64px;border-radius:50%;background:var(--brand)}
.client-name{position:absolute;top:3232px;font-weight:700;color:#111;font-size:26px;line-height:36px;transform:translateX(-50%);white-space:nowrap}

/* footer */
.footer-wave{position:absolute;left:0;top:3355px}
.footer-col h4{position:absolute;top:3545px;font-size:21px;font-weight:500;color:var(--white)}
.footer-about{position:absolute;left:88px;top:3608px;width:330px;font-size:15px;line-height:24px;color:var(--white)}
.footer-link{position:absolute;font-size:15px;font-weight:500;color:var(--white)}
.contact-item{position:absolute;left:943px;font-size:15px;line-height:18px;color:var(--white)}
.contact-icon{position:absolute;left:905px}
.footer-rule{position:absolute;left:0;top:3795px;width:1200px;height:1px;background:var(--sky)}
.copyright{position:absolute;left:0;top:3826px;width:1200px;text-align:center;font-size:16px;color:var(--white)}
</style>
</head>
<body>

<header class="site-header">
  <div class="brand"><span class="brand-dot"></span>VELORIM REPAIR</div>
  <nav class="main-nav">
    <a href="#" style="left:561px">Home</a>
    <a href="#" style="left:637px">About Us</a>
    <a href="#" style="left:744px">Services</a>
    <a href="#" style="left:847px">Gallery</a>
    <a href="#" style="left:941px">Clients</a>
    <a href="#" style="left:1033px">Contact</a>
  </nav>
</header>

<svg class="hero-wave" width="1200" height="520" viewBox="0 0 1200 520" aria-hidden="true">
  <path d="M0 0H1200V400C1130 480 1020 520 900 510C760 500 650 400 520 390C300 380 80 370 0 512Z" fill="var(--wave)"/>
</svg>
<div class="hero-photo" role="img" aria-label="Technician in blue overalls fitting an alloy wheel"></div>
<h1 class="hero-title">Lorem ipsum dolor sit amet, sit consectetur adipiscing</h1>
<p class="hero-text">Lorem ipsum dolor sit amet, consectetur adipiscing elit, sed do eiusmod tempor incididunt ut labore et dolore magna aliqua.</p>
<a class="btn-solid" href="#">Read More</a>

<section class="about">
  <div class="about-panel"></div>
  <div class="about-photo" role="img" aria-label="Polished multi-spoke alloy wheel resting on tyres"></div>
  <h2>About us</h2>
  <p>Lorem ipsum dolor sit amet, consectetur adipiscing elit, sed do eiusmod tempor incididunt ut labore et dolore magna aliqua. Quis ipsum suspendisse ultrices gravida. Risus commodo viverra maecenas accumsan lacus facilisis. Risus commodo viverra maecenas accumsan lacus vel facilisis.</p>
  <a class="btn-outline" href="#">Read More</a>
</section>

<h2 class="section-title" style="top:1398px">Our Services</h2>
<div class="service-card" style="left:91px">
  <div class="thumb" role="img" aria-label="Close-up of alloy wheel with red brake caliper" style="background:linear-gradient(135deg,#9aa1ab,#4b4f57 50%,#b9bec6)"></div>
  <h3>ALLOY WORKS</h3>
</div>
<div class="service-card" style="left:443px">
  <div class="thumb" role="img" aria-label="Grey car fitted with bronze alloy wheels" style="background:linear-gradient(160deg,#a9b4c2,#6e7885 50%,#2e3238)"></div>
  <h3>NEW ALLOYS</h3>
</div>
<div class="service-card" style="left:796px">
  <div class="thumb" role="img" aria-label="High quality polished alloy wheel" style="background:radial-gradient(circle,#d9d9d9,#6d6d6d 45%,#2a2a2a)"></div>
  <h3>HIGH QUALITY</h3>
</div>

<section class="mission">
  <div class="mission-photo" role="img" aria-label="Mechanic kneeling to change a car tyre"></div>
  <h2>Our Mission</h2>
  <p>Lorem ipsum dolor sit amet, consectetur adipiscing elit, sed do eiusmod tempor incididunt ut dolore magna aliqua.</p>
</section>

<h2 class="section-title" style="top:2345px">Our Gallery</h2>
<div class="gallery-item" role="img" aria-label="Black alloy wheel on a white sports car" style="left:79px;top:2450px;width:461px;height:246px;background:linear-gradient(120deg,#2d2f33,#6f747b 50%,#d3d7dc)"></div>
<div class="gallery-item" role="img" aria-label="Silver wheel on a tyre against black background" style="left:569px;top:2450px;width:263px;height:246px;background:radial-gradient(circle,#e7e7e7 0%,#9c9c9c 30%,#151515 55%,#000 100%)"></div>
<div class="gallery-item" role="img" aria-label="Blue car with silver alloy wheel" style="left:859px;top:2450px;width:265px;height:246px;background:linear-gradient(160deg,#2a48b8,#1e2f7a 55%,#8a8f98)"></div>
<div class="gallery-item" role="img" aria-label="Dark alloy wheel with orange brake caliper" style="left:79px;top:2732px;width:261px;height:247px;background:linear-gradient(135deg,#3b4247,#1d2226 50%,#8a5a3a)"></div>
<div class="gallery-item" role="img" aria-label="Technician in blue overalls fitting an alloy wheel" style="left:372px;top:2732px;width:263px;height:247px;background:linear-gradient(90deg,#1d3f8a,#24489c 45%,#b9bcc2)"></div>
<div class="gallery-item" role="img" aria-label="Lime and black wrapped sports car in wet yard" style="left:661px;top:2732px;width:462px;height:247px;background:linear-gradient(180deg,#8a8580,#5c5a55 50%,#3f3a35)"></div>

<h2 class="clients-title">Our Clients</h2>
<div class="carousel-btn" style="left:101px">
  <svg width="64" height="64" viewBox="0 0 64 64" aria-hidden="true"><path d="M36 22L26 32L36 42" stroke="#fff" stroke-width="5" fill="none" stroke-linecap="round" stroke-linejoin="round"/></svg>
</div>
<div class="client-name" style="left:288px;font-size:24px">Brindle Post</div>
<div class="client-name" style="left:490px">Quorla</div>
<div class="client-name" style="left:705px;font-size:44px;top:3222px;line-height:56px">NOLVEX.</div>
<div class="client-name" style="left:940px">TESSORY</div>
<div class="carousel-btn" style="left:1041px">
  <svg width="64" height="64" viewBox="0 0 64 64" aria-hidden="true"><path d="M28 22L38 32L28 42" stroke="#fff" stroke-width="5" fill="none" stroke-linecap="round" stroke-linejoin="round"/></svg>
</div>

<svg class="footer-wave" width="1200" height="543" viewBox="0 0 1200 543" aria-hidden="true">
  <path d="M0 95C80 20 220 -10 330 8C470 30 560 150 720 150C900 150 1080 110 1200 20V543H0Z" fill="var(--wave)"/>
</svg>

<footer>
  <div class="footer-col"><h4 style="left:88px">About Us</h4></div>
  <p class="footer-about">Lorem Ipsum is simply dummy text of the printing and typesetting industry. Lorem Ipsum has been the industry's standard dummy text ever since the 1500s.</p>

  <div class="footer-col"><h4 style="left:463px;top:3541px">Links</h4></div>
  <a class="footer-link" href="#" style="left:463px;top:3590px">About Us</a>
  <a class="footer-link" href="#" style="left:463px;top:3620px">Products</a>
  <a class="footer-link" href="#" style="left:463px;top:3650px">Projects</a>
  <a class="footer-link" href="#" style="left:463px;top:3680px">Contributions</a>
  <a class="footer-link" href="#" style="left:463px;top:3710px">News Privacy</a>

  <div class="footer-col"><h4 style="left:682px;top:3541px">Support</h4></div>
  <a class="footer-link" href="#" style="left:682px;top:3590px">FAQ</a>
  <a class="footer-link" href="#" style="left:682px;top:3619px">How it</a>
  <a class="footer-link" href="#" style="left:682px;top:3648px">Features</a>
  <a class="footer-link" href="#" style="left:682px;top:3677px">Contact</a>
  <a class="footer-link" href="#" style="left:682px;top:3706px">Reporting</a>

  <div class="footer-col"><h4 style="left:902px">Contact</h4></div>
  <svg class="contact-icon" style="top:3596px" width="20" height="20" viewBox="0 0 24 24" aria-hidden="true"><path d="M6.6 10.8a15.1 15.1 0 006.6 6.6l2.2-2.2a1 1 0 011-.25 11.4 11.4 0 003.6.6 1 1 0 011 1V20a1 1 0 01-1 1A17 17 0 013 4a1 1 0 011-1h3.5a1 1 0 011 1c0 1.25.2 2.45.6 3.6a1 1 0 01-.25 1z" fill="#fff"/></svg>
  <div class="contact-item" style="top:3592px">Phone Number<br>+012345679</div>
  <svg class="contact-icon" style="top:3657px" width="20" height="16" viewBox="0 0 24 18" aria-hidden="true"><rect x="1" y="1" width="22" height="16" fill="#fff"/><path d="M1 1L12 10L23 1" stroke="var(--wave)" stroke-width="2" fill="none"/></svg>
  <div class="contact-item" style="top:3651px">Email Address<br>info@yourdomain.com</div>
  <svg class="contact-icon" style="top:3711px;left:908px" width="16" height="22" viewBox="0 0 16 22" aria-hidden="true"><path d="M8 0a8 8 0 00-8 8c0 6 8 14 8 14s8-8 8-14a8 8 0 00-8-8zm0 11a3 3 0 110-6 3 3 0 010 6z" fill="#fff"/></svg>
  <div class="contact-item" style="top:3710px">Office Address<br>Your Address Is Here</div>

  <div class="footer-rule"></div>
  <p class="copyright">Copyright &nbsp;@2030. All Rights Reserved</p>
</footer>

</body>
</html>
```